Online-Marketing Material für Nähmaschinen
Es wurde alles gut umgesetzt und der Kontakt war sehr freundlich und zuverlässig. Danke.
Zielgruppe
Wir verkaufen Nähmaschinen, Stickmaschinen, Overlock und Nähzubehör über unseren Laden und Onlineshop www.Fadenwelt-Haendler.de
Unsere Zielgruppe sind zu 95% Frauen im Alter von 20 - 65 Jahren.
Aufgabenstellung
Wir möchten gerne einen Werbebanner (Bannergröße 2320x540 Pixel) zum Black Friday für unsere Startseite im Onlineshop und Angebotsbilder zu gewissen Maschinen. Bezüglich den Angebotsbilder. Hier sollte bitte eine Umrandung erstellt werden, die wir dann um die Bilder legen können im Photoshop. Der Banner sollte folgendes enthalten.
- WILDE STOFF TAGE (statt Black Friday)
- bis zu 40% sparen
- gültig von 21. - 28.11.2022
Ich habe auch noch unser Firmenlogo und Bilder von Maschinen mit angehängt, die eingebaut werden könnten.
Es ist auch ein alter WILDE STOFF TAGE Banner als Vorlage in welche Richtung es gehen könnte.
Allerdings sind wir an etwas neuem sehr offen.
Viele Grüße
Matthias Lenhart

```html
<!DOCTYPE html>
<html lang="de">
<head>
<meta charset="utf-8">
<title>Wilde Stoff Tage – Fadenwelt Händler</title>
<link rel="stylesheet" href="https://fonts.googleapis.com/css2?family=Arimo:wght@400;700&family=Noto+Sans:wght@400;700&display=swap">
<style>
  :root {
    --bg-dark: #1c1c1e;
    --bg-mid: #2e2e31;
    --glow-red: rgba(229, 16, 42, 0.55);
    --glow-red-soft: rgba(229, 16, 42, 0.35);
    --pill-red: #e5102a;
    --pill-red-deep: #b80d20;
    --text-red: #c8102e;
    --white: #ffffff;
    --tag-black: #0a0a0a;
    --dash-grey: #8a8a8a;
    --tile-bg: #ffffff;
    --product-tone: #e6e6e8;
  }
  html, body {
    margin: 0;
    padding: 0;
    width: 1200px;
    height: 279px;
    overflow: hidden;
    background: var(--bg-dark);
  }
  .banner {
    position: relative;
    width: 1200px;
    height: 279px;
    overflow: hidden;
    background: var(--bg-dark);
    font-family: "Arimo", Arial, sans-serif;
  }
  .backdrop-art {
    position: absolute;
    inset: 0;
    background:
      radial-gradient(ellipse 190px 120px at 120px 40px, var(--glow-red), transparent 70%),
      radial-gradient(ellipse 160px 140px at 290px 240px, var(--glow-red-soft), transparent 70%),
      radial-gradient(ellipse 160px 90px at 940px 60px, var(--glow-red), transparent 70%),
      radial-gradient(ellipse 120px 60px at 800px 270px, var(--glow-red-soft), transparent 70%),
      radial-gradient(ellipse at 55% 45%, var(--bg-mid), var(--bg-dark) 70%);
  }
  .dash-lines { position: absolute; inset: 0; }
  .brand {
    position: absolute;
    left: 74px;
    top: 131px;
    margin: 0;
    color: var(--white);
    font-family: "Arimo", Arial, sans-serif;
    font-weight: 700;
    font-size: 19px;
    line-height: 22px;
    letter-spacing: 0.5px;
    text-transform: uppercase;
  }
  .brand-mark {
    display: inline-block;
    width: 14px;
    height: 14px;
    background: var(--white);
    margin-left: 8px;
    vertical-align: -1px;
  }
  .pill {
    position: absolute;
    left: 543px;
    top: 45px;
    width: 117px;
    height: 27px;
    border-radius: 10px;
    background: linear-gradient(90deg, var(--pill-red-deep), var(--pill-red), var(--pill-red-deep));
  }
  .headline {
    position: absolute;
    left: 318px;
    top: 72px;
    margin: 0;
    white-space: nowrap;
    color: var(--white);
    font-family: "Arimo", Arial, sans-serif;
    font-weight: 400;
    font-size: 54px;
    line-height: 60px;
    letter-spacing: 0.3px;
  }
  .savings {
    position: absolute;
    left: 429px;
    top: 128px;
    margin: 0;
    white-space: nowrap;
    color: var(--text-red);
    font-family: "Noto Sans", sans-serif;
    font-size: 43px;
    line-height: 50px;
    font-weight: 400;
  }
  .savings strong { font-weight: 700; }
  .validity {
    position: absolute;
    left: 676px;
    top: 172px;
    width: 340px;
    height: 40px;
    background: var(--tag-black);
    color: var(--white);
    font-family: "Noto Sans", sans-serif;
    font-size: 25px;
    line-height: 40px;
    text-align: center;
    white-space: nowrap;
    transform: rotate(-7deg);
  }
  .products {
    position: absolute;
    left: 1007px;
    top: 22px;
    display: grid;
    grid-template-columns: 74px 74px;
    grid-auto-rows: 72px;
    column-gap: 8px;
    row-gap: 8px;
  }
  .product-tile {
    background: var(--tile-bg);
    box-shadow: 0 2px 4px rgba(0, 0, 0, 0.5);
    display: flex;
    align-items: center;
    justify-content: center;
  }
  .product-photo {
    width: 62px;
    height: 56px;
    background: radial-gradient(ellipse at 50% 55%, var(--product-tone), var(--tile-bg) 75%);
  }
</style>
</head>
<body>
<div class="banner">
  <div class="backdrop-art" role="img" aria-label="Dunkler Hintergrund mit roten abgerundeten Formen, weißen Punktrastern und feinen Kreislinien"></div>

  <svg class="dash-lines" width="1200" height="279" viewBox="0 0 1200 279" aria-hidden="true">
    <g stroke="var(--dash-grey)" stroke-width="2.5" stroke-dasharray="14 8" fill="none">
      <path d="M0 240 L330 190"/>
      <path d="M915 106 L1007 94"/>
    </g>
  </svg>

  <p class="brand">Fadenwelt<br>Händler<span class="brand-mark"></span></p>

  <div class="pill"></div>
  <h1 class="headline">WILDE STOFF TAGE</h1>
  <p class="savings">bis zu <strong>40%</strong> sparen</p>
  <div class="validity">gültig von 21. - 28.11.2022</div>

  <div class="products">
    <div class="product-tile"><div class="product-photo" role="img" aria-label="Produktfoto: weiße Coverlock-Maschine"></div></div>
    <div class="product-tile"><div class="product-photo" role="img" aria-label="Produktfoto: Overlock-Maschine mit schwarzer Front"></div></div>
    <div class="product-tile"><div class="product-photo" role="img" aria-label="Produktfoto: Stickmaschine mit Stickrahmen"></div></div>
    <div class="product-tile"><div class="product-photo" role="img" aria-label="Produktfoto: weiße Overlock-Maschine mit blauen Akzenten"></div></div>
    <div class="product-tile"><div class="product-photo" role="img" aria-label="Produktfoto: computergesteuerte Nähmaschine"></div></div>
    <div class="product-tile"><div class="product-photo" role="img" aria-label="Produktfoto: weiße Nähmaschine mit Display"></div></div>
  </div>
</div>
</body>
</html>
```